Boutique Store Selling Antiques and Unique Finds

I need a Web Page designed for my Store Called "Harrow Lane". I would like a very classic, muted design that looks European when pulled up. I will be selling Antiques from all over the world and Unique finds that have reproduced. I will also be selling high-end purses and jewelry with unique, reasonable products for the every-day buyer as well.

Target Market(s)

25-70 year old men and women;)

Coding

Number of Pages Required

1 page

Colors

Designer to choose only greyscale colors for use in the design.

Requirements
Must have
• I want it

```html
<!DOCTYPE html>
<html lang="en">
<head>
<meta charset="utf-8">
<title>Harrow Lane — Antiques and Unique Finds</title>
<link href="https://fonts.googleapis.com/css2?family=Cinzel:wght@400;500&family=Jost:wght@400;500&display=swap" rel="stylesheet">
<style>
:root{
  --cream:#efe3c6;
  --cream-light:#f9f5ee;
  --paper:#f4f4f4;
  --ink:#1e1e1e;
  --muted:#444;
  --green:#1f3430;
  --rule:#bcb6aa;
  --black:#000;
  --white:#fff;
}
*{margin:0;padding:0;box-sizing:border-box}
html,body{width:1200px;height:3710px;overflow:hidden}
body{position:relative;background:var(--white);font-family:"Jost",sans-serif;color:var(--ink)}
.abs{position:absolute}
.serif{font-family:"Cinzel",serif}
.photo{position:absolute}
/* header + hero */
.hero{left:0;top:0;width:1200px;height:738px;background:linear-gradient(180deg,#f2e8cf,#eadcb9)}
.nav-link{position:absolute;font-size:14px;color:var(--ink);letter-spacing:.2px}
.nav-rule{position:absolute;height:1px;background:var(--rule)}
.brand{position:absolute;font-family:"Cinzel",serif;font-size:27px;letter-spacing:4px;color:var(--ink);text-align:center}
.hero-card{left:95px;top:269px;width:431px;height:278px;background:var(--cream-light);padding:10px}
.hero-card .frame{width:100%;height:100%;border:1px solid #8d8676;text-align:center;padding-top:44px}
.hero-card h1{font-family:"Cinzel",serif;font-weight:400;font-size:30px;line-height:36px;color:var(--ink)}
.hero-card p{font-size:13.5px;line-height:21px;color:var(--muted);margin:6px 40px 0}
.btn{display:inline-block;background:var(--green);color:var(--white);font-size:13px;font-weight:500;letter-spacing:.4px;text-align:center}
.hero-card .btn{width:141px;height:37px;line-height:37px;margin-top:18px}
/* section titles */
.sec-title{position:absolute;left:0;width:1200px;text-align:center;font-family:"Cinzel",serif;font-size:32px;letter-spacing:3px;color:var(--ink)}
.divider{position:absolute;height:6px}
.divider::before,.divider::after{content:"";position:absolute;top:0;height:4px;width:calc(50% - 18px);border-top:1px solid var(--rule);border-bottom:1px solid var(--rule)}
.divider::before{left:0}.divider::after{right:0}
.divider span{position:absolute;left:50%;top:-3px;width:9px;height:9px;margin-left:-4.5px;background:var(--ink)}
/* product tiles */
.tile{position:absolute;top:897px;width:239px;height:222px}
.tile .label{position:absolute;left:5px;right:5px;bottom:5px;height:40px;background:#eee6d6;text-align:center;line-height:40px;font-family:"Cinzel",serif;font-size:15px;letter-spacing:1.5px}
/* about */
.about-text{left:602px;top:1200px;width:598px;height:490px;background:var(--cream-light);text-align:center}
.about-text .kicker{font-family:"Cinzel",serif;font-size:16px;letter-spacing:2px;margin-top:89px}
.about-text h2{font-family:"Cinzel",serif;font-weight:400;font-size:36px;letter-spacing:3px;margin-top:4px}
.about-text p{font-size:12.5px;line-height:23px;color:var(--muted);margin:0 88px}
/* cards */
.card{position:absolute;border:1px solid #9a9a9a;background:var(--white);text-align:center}
.card .name{font-size:15px;letter-spacing:1px;color:var(--ink)}
.card .price{font-size:14.5px;font-weight:500;margin-top:5px}
.dot{position:absolute;top:2200px;width:8px;height:8px;border-radius:50%;background:#d8d8d8}
.popular{left:0;top:2262px;width:1200px;height:648px;background:var(--paper)}
.dash{display:block;width:18px;height:1px;background:var(--ink);margin:0 auto 14px}
/* newsletter */
.news-title{position:absolute;left:0;top:2993px;width:1200px;text-align:center;font-family:"Cinzel",serif;font-size:25px;line-height:30px;letter-spacing:3px}
.field{position:absolute;top:3099px;height:47px;border:1px solid #999;font-size:12.5px;color:#555;padding-left:19px;line-height:45px}
/* footer */
.footer{left:0;top:3263px;width:1200px;height:447px;background:var(--black);color:var(--white)}
.foot-col{position:absolute;top:176px}
.foot-col h3{font-weight:400;font-size:17px;letter-spacing:.5px;margin-bottom:5px}
.foot-col li{list-style:none;font-size:13px;line-height:25.5px;color:#ddd}
.vrule{position:absolute;top:127px;width:1px;height:255px;background:#2a2a2a}
.small{position:absolute;top:406px;font-size:10px;color:#bbb}
</style>
</head>
<body>

<header class="abs hero">
  <span class="nav-link" style="left:99px;top:24px;font-size:12px">MY ACCOUNT</span>
  <span class="nav-link" style="left:1033px;top:28px;font-size:12px">BASKET (0)</span>
  <div class="nav-rule" style="left:87px;top:58px;width:356px"></div>
  <div class="nav-rule" style="left:759px;top:58px;width:352px"></div>
  <div class="nav-rule" style="left:87px;top:114px;width:356px"></div>
  <div class="nav-rule" style="left:759px;top:114px;width:352px"></div>
  <div class="abs" style="left:87px;top:111px;width:55px;height:3px;background:var(--ink)"></div>
  <span class="nav-link" style="left:95px;top:78px">HOME</span>
  <span class="nav-link" style="left:183px;top:78px">SHOP ONLINE</span>
  <span class="nav-link" style="left:321px;top:78px">PRODUCTS</span>
  <span class="nav-link" style="left:802px;top:78px">DISCOVER</span>
  <span class="nav-link" style="left:914px;top:78px">BLOGS</span>
  <span class="nav-link" style="left:1006px;top:78px">CONTACT US</span>
  <div class="brand" style="left:460px;top:68px;width:290px">Harrow Lane</div>

  <div class="abs hero-card">
    <div class="frame">
      <h1>Antiques from<br>all over the world</h1>
      <p>Lorem ipsum dolor sit amet consectetuer adipiscing elit Nam cursus Morbi ut mi Nullam</p>
      <span class="btn">LEARN MORE</span>
    </div>
  </div>
  <div class="photo" role="img" aria-label="Ornate engraved gold tea set with teapot, sugar bowl and creamer" style="left:576px;top:230px;width:584px;height:360px;background:radial-gradient(ellipse at 50% 55%,#b5803e 0%,#c9984f 45%,rgba(234,220,185,0) 72%)"></div>
</header>

<h2 class="sec-title" style="top:786px">Our Products</h2>
<div class="divider" style="left:455px;top:843px;width:278px"><span></span></div>

<div class="tile" style="left:94px"><div class="photo" role="img" aria-label="Gilded antique dressing table with lamps and mantel clock" style="inset:0;background:linear-gradient(160deg,#2a1d10,#b58c45 55%,#e0c27e)"></div><div class="label">Antiques</div></div>
<div class="tile" style="left:353px"><div class="photo" role="img" aria-label="Brass gramophone horn in a shop of clocks and curios" style="inset:0;background:linear-gradient(160deg,#3b2c1e,#a58537 50%,#4c3a28)"></div><div class="label">Showpiece</div></div>
<div class="tile" style="left:612px"><div class="photo" role="img" aria-label="Brass vase and iron stirrups on a wooden table" style="inset:0;background:linear-gradient(170deg,#4d6b3a,#6b4a30 40%,#8a6744)"></div><div class="label">Purses</div></div>
<div class="tile" style="left:870px"><div class="photo" role="img" aria-label="Ornate gilded antique mantel clock" style="inset:0;background:linear-gradient(160deg,#7a4a26,#9c7a4a 50%,#5a3d22)"></div><div class="label">Jewelry</div></div>

<div class="photo" role="img" aria-label="Tufted velvet sofa with carved gilt frame in a wood-panelled library" style="left:0;top:1200px;width:602px;height:490px;background:linear-gradient(160deg,#3a2415,#7a5638 45%,#b08a62 70%,#4d3422)"></div>
<section class="abs about-text">
  <div class="kicker">About Us</div>
  <h2>Harrow Lane</h2>
  <div class="divider" style="left:156px;top:158px;width:286px"><span></span></div>
  <p style="margin-top:40px">Lorem Ipsum is simply dummy text of the printing and typesetting industry. Lorem Ipsum has been the industry's standard dummy text ever since the 1500s, when an unknown printer.</p>
  <p style="margin-top:12px">It has survived not only five centuries, but also the leap into electronic typesetting, remaining essentially unchanged.</p>
  <span class="btn" style="width:151px;height:39px;line-height:39px;margin-top:24px">LEARN MORE</span>
</section>

<h2 class="sec-title" style="top:1754px">Shop Online</h2>
<div class="divider" style="left:452px;top:1808px;width:280px"><span></span></div>

<div class="card" style="left:94px;top:1853px;width:327px;height:301px"><div class="photo" role="img" aria-label="Brown leather tufted antique sofa" style="left:0;top:0;width:325px;height:221px;background:linear-gradient(170deg,#2c2418,#5a3520 55%,#8a7560)"></div><div style="margin-top:240px" class="name">PRODUCT ANTIQUE CHAIR</div><div class="price">$1,350.00</div></div>
<div class="card" style="left:439px;top:1853px;width:327px;height:301px"><div class="photo" role="img" aria-label="Carved wooden sofa with cream upholstery" style="left:0;top:0;width:325px;height:221px;background:linear-gradient(170deg,#8a5a2a,#d8c29a 50%,#6e2e18)"></div><div style="margin-top:240px" class="name">PRODUCT ANTIQUE CHAIR</div><div class="price">$1,350.00</div></div>
<div class="card" style="left:785px;top:1853px;width:327px;height:301px"><div class="photo" role="img" aria-label="Painted brass bull statue among decorative figurines" style="left:0;top:0;width:325px;height:221px;background:linear-gradient(160deg,#6b5a3a,#b58a3a 45%,#1f7a6e 75%,#5a4a30)"></div><div style="margin-top:240px" class="name">PRODUCT ANTIQUE CHAIR</div><div class="price">$1,350.00</div></div>

<div class="dot" style="left:576px;background:var(--ink)"></div>
<div class="dot" style="left:596px"></div>
<div class="dot" style="left:614px"></div>

<section class="abs popular"></section>
<h2 class="sec-title" style="top:2315px">Poplar Items</h2>
<div class="divider" style="left:475px;top:2368px;width:270px"><span></span></div>

<div class="card" style="left:111px;top:2425px;width:496px;height:400px"><div class="photo" role="img" aria-label="Diamond necklace draped over driftwood" style="left:0;top:0;width:494px;height:305px;background:linear-gradient(160deg,#1e1410,#6b4024 45%,#a87a50 60%,#2a1c14)"></div><div style="margin-top:318px"><span class="dash"></span><div class="name">MURANO CARAFE GOLD SWIRL</div><div class="price">$1,350.00</div></div></div>
<div class="card" style="left:628px;top:2425px;width:496px;height:400px"><div class="photo" role="img" aria-label="Designer handbag with gold clasp on a glass shelf" style="left:0;top:0;width:494px;height:305px;background:linear-gradient(170deg,#e8c8b0,#d0b890 45%,#3a3a3a 70%,#cfc6bc)"></div><div style="margin-top:318px"><span class="dash"></span><div class="name">MURANO CARAFE GOLD SWIRL</div><div class="price">$1,350.00</div></div></div>

<h2 class="news-title">Sign up to our newsletter<br>to stay up to date</h2>
<div class="field" style="left:176px;width:325px">Your Name</div>
<div class="field" style="left:514px;width:326px">Your Email address</div>
<span class="btn abs" style="left:851px;top:3098px;width:176px;height:48px;line-height:48px;font-size:14px;letter-spacing:2px">SUBSCRIBE</span>

<footer class="abs footer">
  <div class="brand" style="left:455px;top:40px;width:290px;color:var(--white)">Harrow Lane</div>
  <div class="abs" style="left:0;top:127px;width:1200px;height:1px;background:#2a2a2a"></div>
  <div class="vrule" style="left:373px"></div>
  <div class="vrule" style="left:666px"></div>
  <div class="vrule" style="left:919px"></div>
  <div class="abs" style="left:0;top:382px;width:1200px;height:1px;background:#2a2a2a"></div>
  <div class="foot-col" style="left:167px"><h3>ABOUT US</h3><ul><li>A Family Business</li><li>Philosophy and Ethos</li><li>Charity and Community</li><li>Press</li><li>Careers</li></ul></div>
  <div class="foot-col" style="left:429px"><h3>SPECIAL EVENTS</h3><ul><li>Workshops</li><li>Private Events Richmond</li><li>Private Events Covent Garden</li><li>Supper Clubs</li></ul></div>
  <div class="foot-col" style="left:738px"><h3>RESOURCES</h3><ul><li>Terms and Conditions</li><li>Privacy Policy</li><li>Contact</li></ul></div>
  <div class="foot-col" style="left:987px"><h3>SOCIAL</h3><ul><li>Photo Feed</li><li>Friends Page</li><li>Pin Board</li><li>Short Posts</li></ul></div>
  <span class="small" style="left:182px">2021 © Harrow Lane &nbsp;|&nbsp; All Right Reserved</span>
  <span class="small" style="left:886px">Cookies</span>
  <span class="small" style="left:941px">Sitemap</span>
  <span class="small" style="left:998px">Terms of Use</span>
</footer>

</body>
</html>
```